Wine label refresh

We are wanting to modify our Corran Estate label to include a picture on it.
I have attached the pictures below which we would like on the label. They are of the Corran Estate vineyard. I have also attached an example of another label with a picture on it that we like the style of.
Industry/Entity Type
Vineyard
Requirements
Must have
- The Corran Estate text must stay the same but can be moved down. It still needs to be the same size though.
Marlborough Sauvignon Blanc should remain in the same font and roughly the same size.
Wine of New Zealand also must stay but could potentially be moved.
Nice to have
- It would be nice if we could keep the KL logo on the front label but feel free to experiment with where this goes.

```html
<!DOCTYPE html>
<html lang="en">
<head>
<meta charset="utf-8">
<title>Corran Estate – Marlborough Sauvignon Blanc label</title>
<link rel="stylesheet" href="https://fonts.googleapis.com/css2?family=Cormorant+Garamond:ital,wght@0,500;1,500&family=Pinyon+Script&family=Lato:wght@400&display=swap">
<style>
  :root {
    --backdrop: #e9e8e4;
    --label-paper: #f4f2ec;
    --wine-red: #7a1f2b;
    --monogram-grey: #7b7b7b;
    --gold: #c9a23a;
    --band-blue: #7d93a6;
    --band-text: #f3f5f7;
    --scene-green: #4f6a3a;
    --scene-sky: #b9c4c4;
    --scene-dark: #2f3f28;
  }
  html, body {
    margin: 0;
    padding: 0;
    width: 1035px;
    height: 1200px;
    overflow: hidden;
    background: var(--backdrop);
  }
  .canvas {
    position: relative;
    width: 1035px;
    height: 1200px;
  }
  .label {
    position: absolute;
    left: 137px;
    top: 60px;
    width: 760px;
    height: 1080px;
    background: var(--label-paper);
    box-shadow: 0 2px 14px rgba(0,0,0,0.12);
    overflow: hidden;
  }
  .brand-mark {
    position: absolute;
    top: 80px;
    left: 0;
    width: 100%;
    text-align: center;
    font-family: "Cormorant Garamond", serif;
    font-weight: 500;
    font-size: 64px;
    letter-spacing: 4px;
    color: var(--monogram-grey);
  }
  .estate-name {
    position: absolute;
    top: 222px;
    left: 0;
    width: 100%;
    text-align: center;
    font-family: "Cormorant Garamond", serif;
    font-weight: 500;
    font-size: 64px;
    font-variant: small-caps;
    letter-spacing: 3px;
    color: var(--wine-red);
  }
  .vineyard-photo {
    position: absolute;
    top: 360px;
    left: 110px;
    width: 540px;
    height: 230px;
    background: linear-gradient(180deg, var(--scene-sky) 0%, var(--scene-dark) 38%, var(--scene-green) 70%, var(--scene-dark) 100%);
  }
  .gold-rule {
    position: absolute;
    top: 590px;
    left: 110px;
    width: 540px;
    height: 12px;
    background: var(--gold);
  }
  .varietal {
    position: absolute;
    top: 680px;
    left: 0;
    width: 100%;
    text-align: center;
    font-family: "Pinyon Script", cursive;
    font-size: 64px;
    color: var(--wine-red);
  }
  .vintage {
    position: absolute;
    top: 790px;
    left: 0;
    width: 100%;
    text-align: center;
    font-family: "Cormorant Garamond", serif;
    font-style: italic;
    font-weight: 500;
    font-size: 54px;
    letter-spacing: 3px;
    color: var(--wine-red);
  }
  .info-band {
    position: absolute;
    left: 0;
    bottom: 0;
    width: 100%;
    height: 140px;
    background: var(--band-blue);
    display: flex;
    align-items: center;
    justify-content: space-between;
    padding: 0 34px;
    box-sizing: border-box;
    font-family: "Lato", sans-serif;
    color: var(--band-text);
  }
  .info-band .volume,
  .info-band .strength {
    font-size: 22px;
  }
  .info-band .origin {
    font-size: 32px;
    letter-spacing: 1px;
  }
</style>
</head>
<body>
<main class="canvas">
  <section class="label">
    <div class="brand-mark">KL</div>
    <h1 class="estate-name" style="margin:0">Corran Estate</h1>
    <div class="vineyard-photo" role="img" aria-label="Photograph of the Corran Estate vineyard with palm trees, a homestead and vine rows under a pale sky"></div>
    <div class="gold-rule"></div>
    <div class="varietal">Marlborough Sauvignon Blanc</div>
    <div class="vintage">2012</div>
    <footer class="info-band">
      <span class="volume">750ml</span>
      <span class="origin">NEW ZEALAND WINE</span>
      <span class="strength">13% alc/vol</span>
    </footer>
  </section>
</main>
</body>
</html>
```